70s 80s Revival club night

Hi,

I'm look for a poster design for a 70s & 80s revival club night.
The design must say thr following...

Velvet Grooves
70s & 80s Revival Club Night.

Also, must incorporate our company logo (Attached)

```html
<!DOCTYPE html>
<html lang="en">
<head>
<meta charset="utf-8">
<title>Velvet Grooves – 70s &amp; 80s Revival Club Night</title>
<link rel="stylesheet" href="https://fonts.googleapis.com/css2?family=Oswald:wght@500;700&family=Fredoka:wght@700&family=Roboto:ital,wght@1,900&family=Montserrat:wght@600;700;800&display=swap">
<style>
  :root {
    --magenta: #e8397a;
    --crimson: #d92a3c;
    --plum: #4a1e5c;
    --deep-plum: #2c1640;
    --ink-purple: #3a1850;
    --rose-edge: #c8347a;
    --white: #ffffff;
    --ribbon-red: #e53a3a;
    --ribbon-dark: #a81f2c;
  }
  * { margin: 0; padding: 0; box-sizing: border-box; }
  html, body { width: 776px; height: 1200px; overflow: hidden; background: var(--deep-plum); }

  .poster {
    position: relative;
    width: 776px;
    height: 1200px;
    overflow: hidden;
    background:
      radial-gradient(circle at 400px 470px, #3b1a4e 0 150px, transparent 152px),
      radial-gradient(circle at 400px 470px, #7a2552 0 230px, transparent 232px),
      radial-gradient(circle at 400px 470px, #a52a4c 0 330px, transparent 332px),
      radial-gradient(circle at 400px 470px, #c8304a 0 460px, transparent 462px),
      linear-gradient(160deg, #e8406e 0%, #d22f4a 35%, #8a2a66 70%, #3a1a55 100%);
  }

  .dancers {
    position: absolute;
    left: 0; right: 0; bottom: 0;
    height: 360px;
    background: linear-gradient(180deg, rgba(58,24,80,0) 0%, rgba(150,60,140,0.45) 40%, rgba(120,50,140,0.6) 70%, rgba(40,20,60,0.9) 100%);
  }

  .organiser {
    position: absolute;
    top: 86px; left: 0; width: 776px;
    padding-left: 60px;
    text-align: center;
    font-family: 'Oswald', sans-serif;
    font-weight: 500;
    font-size: 52px;
    letter-spacing: 7px;
    color: var(--white);
    line-height: 1;
  }

  .decades {
    font-family: 'Fredoka', sans-serif;
    font-weight: 700;
    color: var(--white);
    position: absolute;
    line-height: 1;
    transform-origin: left top;
    text-shadow:
      2px 2px 0 var(--rose-edge),
      4px 5px 0 #b02a6a,
      6px 8px 0 #8a2058,
      8px 11px 0 #6a1848;
    -webkit-text-stroke: 2px #f2c6dc;
  }
  .decades--seventies { top: 140px; left: 116px; font-size: 245px; letter-spacing: -4px; transform: scaleX(1.18); }
  .decades--amp { top: 245px; left: 505px; font-size: 120px; }
  .decades--eighties { top: 320px; left: 182px; font-size: 255px; letter-spacing: -4px; transform: scaleX(1.15); }

  .headline {
    position: absolute;
    left: 0; width: 776px;
    text-align: center;
    font-family: 'Oswald', sans-serif;
    font-weight: 700;
    color: var(--white);
    line-height: 1;
    text-transform: uppercase;
    text-shadow: 2px 3px 0 var(--rose-edge), 4px 6px 0 #8a2058;
  }
  .headline--revival { top: 565px; padding-left: 20px; font-size: 128px; transform: rotate(-4deg); letter-spacing: 1px; }
  .headline--club { top: 685px; padding-left: 20px; font-size: 84px; transform: rotate(-4deg); }

  .date-ribbon {
    position: absolute;
    top: 805px; left: 120px;
    width: 510px; height: 66px;
    transform: rotate(-8deg);
  }
  .date-ribbon svg { position: absolute; inset: 0; }
  .date-ribbon__text {
    position: absolute;
    inset: 0;
    display: flex; align-items: center; justify-content: center;
    font-family: 'Roboto', sans-serif;
    font-style: italic;
    font-weight: 900;
    font-size: 29px;
    color: var(--white);
    text-shadow: 1px 2px 0 rgba(90,10,30,0.5);
  }

  .brand {
    position: absolute;
    top: 1004px; left: 0; width: 776px;
    text-align: center;
    color: var(--white);
  }
  .brand__mark {
    display: inline-flex; align-items: center; gap: 12px;
    font-family: 'Montserrat', sans-serif;
    font-weight: 800;
    font-size: 32px;
    letter-spacing: 1px;
    text-transform: uppercase;
  }
  .brand__dot {
    width: 22px; height: 22px; border-radius: 50%;
    background: var(--ribbon-red);
  }

  .details {
    position: absolute;
    top: 1070px; left: 0; width: 776px;
    text-align: center;
    font-family: 'Montserrat', sans-serif;
    font-weight: 700;
    font-size: 26px;
    letter-spacing: 2.5px;
    line-height: 35px;
    color: var(--white);
  }
</style>
</head>
<body>
  <main class="poster">
    <div class="dancers" role="img" aria-label="Silhouettes of people dancing in retro disco style"></div>

    <p class="organiser">VELVET GROOVES</p>

    <h1 class="event-title">
      <span class="decades decades--seventies">70s</span>
      <span class="decades decades--amp">&amp;</span>
      <span class="decades decades--eighties">80s</span>
      <span class="headline headline--revival">Revival</span>
      <span class="headline headline--club">Club Night</span>
    </h1>

    <div class="date-ribbon">
      <svg width="510" height="66" viewBox="0 0 510 66" aria-hidden="true">
        <polygon points="0,4 510,0 492,33 510,66 0,62 18,33" fill="var(--ribbon-red)"/>
        <polygon points="0,62 510,66 510,60 6,56" fill="var(--ribbon-dark)"/>
      </svg>
      <p class="date-ribbon__text">Saturday 8th April 2023 at 8pm</p>
    </div>

    <div class="brand">
      <div class="brand__mark"><span class="brand__dot"></span>Velvet Grooves</div>
    </div>

    <p class="details">Kestrel Arts Centre, Main Space<br>Fancy dress strongly encouraged!</p>
  </main>
</body>
</html>
```